Visitenkarten-Design für Garten- und Landschaftspflege
Tamuga Vent setzte meine Vorstellungen absolut super um ich kann Ihn nur weiter empfehlen. vielen dank
Zielgruppe
Baumpflege, Baumfällung, Garten und Landschaftspflege meine zielgruppe sind Privatpersonen im alter von 20-100Jahren
Aufgabenstellung
Sehr geehrte Damen und Herren, die visitenkarte sollte die angaben so enthalten wie sie auf der von mir gestallteten Visitenkarten sind ( meine ist kein maß der Dinge). Ich habe mein Logo leider nur als 3.jpg Datei. Das Logo darf im Design erändert werden aber bitte nur Feinheiten ansonsten stehen ihnen alle türen offen um kreativ zu sein.
mit freundlichen Grüßen Holger Banzow

```html
<!DOCTYPE html>
<html lang="de">
<head>
<meta charset="utf-8">
<title>Visitenkarte Baumpflege Banzow</title>
<link href="https://fonts.googleapis.com/css2?family=Arimo:wght@400&family=Michroma&display=swap" rel="stylesheet">
<style>
  :root {
    --bg: #eeeeee;
    --paper: #fbfbfb;
    --green-dark: #0f7232;
    --green-light: #2f8a55;
    --edge: #2b2b2b;
    --ink: #333333;
    --white: #ffffff;
    --back-dark: #2f2f2f;
    --back-light: #565656;
    --header: #1c1c1c;
    --list-text: #e6e6e6;
  }
  * { box-sizing: border-box; margin: 0; padding: 0; }
  html, body {
    width: 1200px; height: 864px; overflow: hidden;
    background: var(--bg);
    font-family: "Arimo", Arial, sans-serif;
  }
  .cards {
    position: absolute; top: 264px; left: 60px;
    display: flex; gap: 40px;
  }
  .card {
    position: relative; width: 520px; height: 336px; overflow: hidden;
    box-shadow: 0 6px 18px rgba(0,0,0,.18);
  }

  /* Front */
  .card--front { background: var(--paper); }
  .front__band {
    position: absolute; left: 0; right: 0; top: 158px; bottom: 0;
    background: linear-gradient(120deg, var(--green-dark), var(--green-light));
    border-top: 3px solid var(--edge);
  }
  .person { position: absolute; left: 320px; top: 60px; }
  .person__name { color: var(--green-dark); font-size: 18px; }
  .person__role { color: var(--ink); font-size: 12px; line-height: 15px; margin-top: 6px; }
  .brand {
    position: absolute; left: 44px; top: 184px;
    display: flex; align-items: center; gap: 10px;
    font-family: "Arimo", Arial, sans-serif; font-weight: 400;
    color: var(--white); font-size: 26px; line-height: 1;
  }
  .brand__mark { width: 14px; height: 14px; background: var(--white); flex: none; }
  .contact { position: absolute; left: 44px; top: 244px; list-style: none; }
  .contact li, .address {
    display: flex; align-items: center; gap: 8px;
    color: var(--white); font-size: 11.5px; line-height: 23px;
  }
  .contact svg, .address svg { width: 14px; height: 14px; flex: none; }
  .address { position: absolute; left: 360px; top: 278px; align-items: flex-start; line-height: 16px; }

  /* Back */
  .card--back { background: linear-gradient(100deg, var(--back-dark), var(--back-light)); }
  .back__header {
    position: absolute; left: 0; right: 0; top: 0; height: 46px;
    background: var(--header); border-bottom: 2px solid #444;
    display: flex; align-items: center; justify-content: flex-end; padding-right: 26px;
  }
  .back__title {
    font-family: "Michroma", sans-serif; color: var(--white);
    font-size: 20px; letter-spacing: 3px; font-weight: 400;
  }
  .services { position: absolute; left: 40px; top: 64px; list-style: none; }
  .services li {
    display: flex; align-items: center; gap: 8px;
    color: var(--list-text); font-size: 13px; line-height: 21px;
  }
  .services svg { width: 9px; height: 9px; flex: none; }
</style>
</head>
<body>
<main class="cards">
  <section class="card card--front" aria-label="Vorderseite">
    <div class="front__band"></div>
    <div class="person">
      <p class="person__name">Holger Banzow</p>
      <p class="person__role">Fachagrarwirt Baumpflege/<br>Baumsanierung</p>
    </div>
    <p class="brand"><span class="brand__mark"></span>Baumpflege Banzow</p>
    <ul class="contact">
      <li><svg viewBox="0 0 16 16"><path fill="#fff" d="M3 1.5l3 2.5-1.3 2a8 8 0 0 0 5.3 5.3l2-1.3 2.5 3-1.8 1.8C7 14.5 1.5 9 1.2 3.3z"/></svg>01 70 / 55 21 904</li>
      <li><svg viewBox="0 0 16 16"><rect x="1" y="3" width="14" height="10" fill="none" stroke="#fff" stroke-width="1.3"/><path d="M1 3l7 6 7-6" fill="none" stroke="#fff" stroke-width="1.3"/></svg>kontakt@baumpflege-banzow.de</li>
      <li><svg viewBox="0 0 16 16"><circle cx="8" cy="8" r="6.5" fill="none" stroke="#fff" stroke-width="1.3"/><path d="M1.5 8h13M8 1.5c-3 3.5-3 9.5 0 13M8 1.5c3 3.5 3 9.5 0 13" fill="none" stroke="#fff" stroke-width="1.1"/></svg>www.baumpflege-banzow.de</li>
    </ul>
    <div class="address">
      <svg viewBox="0 0 16 16"><path fill="none" stroke="#fff" stroke-width="1.5" d="M8 15s5-5.5 5-9A5 5 0 0 0 3 6c0 3.5 5 9 5 9z"/><circle cx="8" cy="6" r="1.8" fill="#fff"/></svg>
      <span>Lindenweg 12<br>85599 Holzfeld</span>
    </div>
  </section>

  <section class="card card--back" aria-label="Rückseite">
    <header class="back__header"><h2 class="back__title">UNSERE LEISTUNGEN</h2></header>
    <ul class="services">
      <li><svg viewBox="0 0 10 10"><circle cx="5" cy="5" r="4.3" fill="none" stroke="#ddd"/><path d="M3 5.2l1.5 1.4L7 4" fill="none" stroke="#ddd"/></svg>Neupflanzungen</li>
      <li><svg viewBox="0 0 10 10"><circle cx="5" cy="5" r="4.3" fill="none" stroke="#ddd"/><path d="M3 5.2l1.5 1.4L7 4" fill="none" stroke="#ddd"/></svg>Herstellung der Verkehrssicherheit von Bäumen</li>
      <li><svg viewBox="0 0 10 10"><circle cx="5" cy="5" r="4.3" fill="none" stroke="#ddd"/><path d="M3 5.2l1.5 1.4L7 4" fill="none" stroke="#ddd"/></svg>Kronenrückschnitt (Einkürzung &amp; Kronenpflege)</li>
      <li><svg viewBox="0 0 10 10"><circle cx="5" cy="5" r="4.3" fill="none" stroke="#ddd"/><path d="M3 5.2l1.5 1.4L7 4" fill="none" stroke="#ddd"/></svg>Standsicherheitsprüfung von Bäumen</li>
      <li><svg viewBox="0 0 10 10"><circle cx="5" cy="5" r="4.3" fill="none" stroke="#ddd"/><path d="M3 5.2l1.5 1.4L7 4" fill="none" stroke="#ddd"/></svg>Baumfällung</li>
      <li><svg viewBox="0 0 10 10"><circle cx="5" cy="5" r="4.3" fill="none" stroke="#ddd"/><path d="M3 5.2l1.5 1.4L7 4" fill="none" stroke="#ddd"/></svg>Obstbaumschnitt</li>
      <li><svg viewBox="0 0 10 10"><circle cx="5" cy="5" r="4.3" fill="none" stroke="#ddd"/><path d="M3 5.2l1.5 1.4L7 4" fill="none" stroke="#ddd"/></svg>Wurzelstock-Fräsung</li>
      <li><svg viewBox="0 0 10 10"><circle cx="5" cy="5" r="4.3" fill="none" stroke="#ddd"/><path d="M3 5.2l1.5 1.4L7 4" fill="none" stroke="#ddd"/></svg>professionelle Anfertigung &amp; Aufbau von Gartenhäusern nach Maß</li>
    </ul>
  </section>
</main>
</body>
</html>
```